Stylist/Barber Standup Sign for Hair Regrowth Company

We want to design an attractive and eye-catching sign for hair stylists and barbers to sit on their workstations to attract the attention of their clients regarding hair loss and encourage them to speak to their stylist about it of they are would like to seek treatment.
50% of men and 25% of women suffer from hair loss but most are in denial that it is happening or too embarrassed to talk about it.

Copy for the flyer is as follows:

[Section 1:]
This flyer has been placed here/designed to spark conversation about hair loss

[Section 2:]
The truth is...
73% of people believe their hair is thinning
They are right

[Section 3:]
If you've got questions, your stylist or barber has answers.

Additional Background Information:

Primary target audience is men between the ages of 25-45, secondary target audience is men 46-60

Current Consumer Perception? (in the first person) “I’ve been thinking about my hair. I think it’s getting thinner and I’m scared, worried and don’t know what to do. But I don’t know if there is anything that really works. I’ve tried other things and nothing‘s worked.”

Tonality of materials? Very guy friendly, matter of fact, authoritative, its what you might hear from your best friend. Confident. Encouraging, but with a sense of urgency.

Please use our brand colors, but do not include our logo or brand name.
Colors are as follows:
Green: #4ca26f
Light Grey: #999999
Dark Grey: #262626

I have attached print templates in both PDF and Jpeg, please use those to provide final ready to print documents if you are selected.

Target Market(s)

Industry/Entity Type

Health And Wellness

Font styles to use
Sans Serif

Colors
00a990
ffffff
333333
cbcbcb

Requirements
Must have
• We want to get across the following messaging. Ideally you will submit a design using our copy and if you think you can do better, please feel free to submit another design with your own copy/messaging. If you can do it better we would love to select you :-)
• Our copy?
• This flyer has been placed here/designed to spark conversation about hair loss
• The truth is...
• 73% of people believe their hair is thinning
• They are right
• If you've got questions, your stylist or barber has answers
• Also please use our brand colors:
• Green: #4ca26f
• Light Grey: #999999
• Dark Grey: #262626
Should not have
• dont add any logos, images or ornate design. this needs to be simple, easy to ready and eye catching.
• do not use the color red in any capacity.

```html
<!DOCTYPE html>
<html lang="en">
<head>
<meta charset="utf-8">
<title>Hair Loss Conversation Sign</title>
<link href="https://fonts.googleapis.com/css2?family=Open+Sans:wght@400;700;800&display=swap" rel="stylesheet">
<style>
  :root {
    --teal: #00a990;
    --white: #ffffff;
    --ink: #333333;
    --mist: #cbcbcb;
    --backdrop: #efefed;
  }
  html, body {
    margin: 0;
    padding: 0;
    width: 1200px;
    height: 1200px;
    overflow: hidden;
    background: var(--backdrop);
  }
  .canvas {
    position: relative;
    width: 1200px;
    height: 1200px;
  }
  .sign {
    position: absolute;
    top: 214px;
    width: 522px;
    height: 771px;
    background: var(--white);
  }
  .sign--dark { left: 53px; }
  .sign--light { left: 626px; }
  .sign svg { display: block; width: 522px; height: 771px; }
  text { font-family: "Open Sans", sans-serif; text-anchor: middle; }
  .band { fill: var(--teal); }
  .kicker { fill: var(--white); font-weight: 800; font-size: 24px; }
  .intro { fill: var(--ink); font-weight: 800; font-size: 30px; }
  .headline { fill: var(--teal); font-weight: 800; font-size: 76px; }
  .quote-bubble { fill: var(--mist); }
  .quote-line { fill: var(--ink); font-weight: 700; font-size: 19.5px; }
  .quote-mark { fill: var(--white); font-weight: 800; font-size: 72px; text-anchor: start; }
  .truth-bubble--dark { fill: var(--ink); }
  .truth-bubble--light { fill: var(--white); stroke: var(--ink); stroke-width: 4; }
  .truth-lead { font-weight: 800; font-size: 46px; }
  .truth-figure { font-weight: 800; font-size: 56px; }
  .truth-note { font-weight: 400; font-size: 21px; }
  .truth-verdict { fill: var(--teal); font-weight: 800; font-size: 48px; }
  .sign--dark .truth-lead { fill: var(--mist); }
  .sign--dark .truth-figure, .sign--dark .truth-note { fill: var(--white); }
  .sign--light .truth-lead, .sign--light .truth-figure, .sign--light .truth-note { fill: var(--ink); }
  .cta { fill: var(--white); font-weight: 800; font-size: 33px; }
</style>
</head>
<body>
<main class="canvas">

  <section class="sign sign--dark">
    <svg viewBox="0 0 522 771" xmlns="http://www.w3.org/2000/svg">
      <rect class="band" x="0" y="0" width="522" height="54"/>
      <text class="kicker" x="261" y="36">THIS FLYER HAS BEEN PLACED HERE</text>
      <text class="intro" x="261" y="82">DESIGNED TO SPARK</text>
      <text class="intro" x="261" y="112">CONVERSATION ABOUT</text>
      <text class="headline" x="261" y="185">HAIR LOSS</text>

      <path class="quote-bubble" d="M10,206 H462 Q490,206 490,234 V318 Q490,346 462,346 H62 Q34,346 34,318 V240 Q34,220 10,206 Z"/>
      <text class="quote-mark" x="34" y="272">“</text>
      <text class="quote-line" x="267" y="246">I THINK MY HAIR GETTING THINNER.</text>
      <text class="quote-line" x="267" y="287">I’M WORRIED AND</text>
      <text class="quote-line" x="253" y="328">I DON’T KNOW WHAT TO DO.</text>
      <text class="quote-mark" x="424" y="364">”</text>

      <path class="truth-bubble--dark" d="M58,362 H514 Q490,380 490,412 V561 Q490,585 466,585 H58 Q34,585 34,561 V386 Q34,362 58,362 Z"/>
      <text class="truth-lead" x="261" y="422">THE TRUTH IS...</text>
      <text class="truth-figure" x="261" y="474">73%</text>
      <text class="truth-note" x="261" y="502">of people believe their hair is thinning</text>
      <text class="truth-verdict" x="261" y="562">THEY ARE RIGHT</text>

      <rect class="band" x="0" y="606" width="522" height="165"/>
      <text class="cta" x="261" y="655">IF YOU’VE GOT QUESTIONS,</text>
      <text class="cta" x="261" y="696">YOUR STYLIST OR BARBER</text>
      <text class="cta" x="261" y="737">HAS ANSWERS</text>
    </svg>
  </section>

  <section class="sign sign--light">
    <svg viewBox="0 0 522 771" xmlns="http://www.w3.org/2000/svg">
      <rect class="band" x="0" y="0" width="522" height="54"/>
      <text class="kicker" x="261" y="36">THIS FLYER HAS BEEN PLACED HERE</text>
      <text class="intro" x="261" y="82">DESIGNED TO SPARK</text>
      <text class="intro" x="261" y="112">CONVERSATION ABOUT</text>
      <text class="headline" x="261" y="185">HAIR LOSS</text>

      <path class="quote-bubble" d="M10,201 H462 Q490,201 490,229 V313 Q490,341 462,341 H62 Q34,341 34,313 V235 Q34,215 10,201 Z"/>
      <text class="quote-mark" x="34" y="267">“</text>
      <text class="quote-line" x="267" y="241">I THINK MY HAIR GETTING THINNER.</text>
      <text class="quote-line" x="267" y="282">I’M WORRIED AND</text>
      <text class="quote-line" x="253" y="323">I DON’T KNOW WHAT TO DO.</text>
      <text class="quote-mark" x="424" y="359">”</text>

      <path class="truth-bubble--light" d="M58,362 H512 Q490,380 490,412 V561 Q490,585 466,585 H58 Q34,585 34,561 V386 Q34,362 58,362 Z"/>
      <text class="truth-lead" x="261" y="422">THE TRUTH IS...</text>
      <text class="truth-figure" x="261" y="474">73%</text>
      <text class="truth-note" x="261" y="502">of people believe their hair is thinning</text>
      <text class="truth-verdict" x="261" y="562">THEY ARE RIGHT</text>

      <rect class="band" x="0" y="606" width="522" height="165"/>
      <text class="cta" x="261" y="655">IF YOU’VE GOT QUESTIONS,</text>
      <text class="cta" x="261" y="696">YOUR STYLIST OR BARBER</text>
      <text class="cta" x="261" y="737">HAS ANSWERS</text>
    </svg>
  </section>

</main>
</body>
</html>
```